Construction company needs upscale elegant truck and trailer design

Hello,
I am looking for a wrap design for my Veldrin marlow truck and my 6x12 cargo trailer. I want to advertise my remodeling business, but I want it to be elegant and upscale. We work on commercial and residential projects with a specialization in historic homes and interior buildouts.
Our website is www.brisketonbuilders.example.
We cater to upscale clientele and I don't want it to be too flashy. I don't want anything on the back glass. I also don't want a full vehicle wrap to keep the cost down. I want a partial wrap that goes towards the back, nothing on the hood. The phone number is 555-318-2947.

Target Market(s)

Historic Restoration - New Construction - Remodeling

Industry/Entity Type

Luxury Construction Remodeling

Colors

Designer to choose colors to be used in the design.

Requirements
Must have
• truck and trailer
Nice to have
• My truck is silver with black rims, so I want it to match nice with what I already have.

```html
<!DOCTYPE html>
<html lang="en">
<head>
<meta charset="UTF-8">
<title>Brisketon Builders – Truck &amp; Trailer Graphics</title>
<link href="https://fonts.googleapis.com/css2?family=Tinos:wght@700&family=Jost:ital,wght@1,800&family=Marcellus&display=swap" rel="stylesheet">
<style>
  :root {
    --canvas: #eeeeee;
    --panel: #ffffff;
    --ink: #231f20;
    --rule: #6d6d6d;
    --muted: #4a4a4a;
  }
  * { margin: 0; padding: 0; box-sizing: border-box; }
  html, body { width: 1200px; height: 1200px; overflow: hidden; }
  body { background: var(--canvas); position: relative; font-family: "Tinos", "Times New Roman", serif; color: var(--ink); }

  .panel { position: absolute; background: var(--panel); box-shadow: 0 2px 10px rgba(0,0,0,0.12); overflow: hidden; }

  .company-name { font-family: "Tinos", "Times New Roman", serif; font-weight: 700; text-align: center; line-height: 1; color: var(--ink); }
  .company-name .line-1 { display: block; letter-spacing: 0.04em; }
  .company-name .line-2 { display: block; letter-spacing: 0.02em; }

  .phone { font-family: "Jost", "Futura", sans-serif; font-style: italic; font-weight: 800; color: var(--ink); line-height: 1; }
  .web { font-family: "Marcellus", "Optima", serif; }

  /* Truck door panel */
  .truck-panel { left: 100px; top: 150px; width: 1000px; height: 278px; }
  .truck-panel .company-name { position: absolute; left: 50px; top: 82px; width: 500px; }
  .truck-panel .line-1 { font-size: 64px; }
  .truck-panel .line-2 { font-size: 44px; margin-top: 12px; }
  .truck-panel .contact { position: absolute; left: 580px; top: 92px; width: 360px; text-align: center; }
  .truck-panel .phone { font-size: 38px; }
  .truck-panel .web-pill { display: inline-block; margin-top: 6px; background: var(--ink); color: #fff; border-radius: 16px; padding: 3px 22px; font-size: 24px; }
  .truck-panel .license { margin-top: 10px; font-family: "Marcellus", serif; font-size: 15px; color: var(--muted); letter-spacing: 0.02em; }
  .truck-panel .swoosh { position: absolute; left: 0; top: 238px; width: 1000px; height: 16px; }

  /* Trailer side panel */
  .trailer-panel { left: 190px; top: 520px; width: 820px; height: 400px; }
  .trailer-panel .company-name { position: absolute; left: 60px; top: 78px; width: 700px; }
  .trailer-panel .line-1 { font-size: 74px; }
  .trailer-panel .line-2 { font-size: 56px; margin-top: 8px; }
  .trailer-panel .web-line { position: absolute; left: 66px; top: 236px; width: 690px; border-top: 1.5px solid var(--rule); border-bottom: 1.5px solid var(--rule); padding: 8px 0 10px; text-align: center; font-size: 21px; color: var(--muted); letter-spacing: 0.01em; }
  .trailer-panel .bar { position: absolute; left: 0; top: 311px; width: 820px; height: 12px; }
  .trailer-panel .phone { position: absolute; right: 26px; top: 298px; background: var(--panel); padding: 0 10px; font-size: 30px; }
</style>
</head>
<body>

  <section class="panel truck-panel" aria-label="Truck door graphic">
    <h1 class="company-name">
      <span class="line-1">BRISKETON</span>
      <span class="line-2">BUILDERS</span>
    </h1>
    <div class="contact">
      <div class="phone">555-318-2947</div>
      <div class="web web-pill">BrisketonBuilders.example</div>
      <div class="license">Certified Building Contractor #048173</div>
    </div>
    <svg class="swoosh" viewBox="0 0 1000 16" preserveAspectRatio="none" aria-hidden="true">
      <polygon points="110,14 150,5 1000,2 1000,10 150,14" fill="var(--ink)"/>
    </svg>
  </section>

  <section class="panel trailer-panel" aria-label="Trailer side graphic">
    <h2 class="company-name">
      <span class="line-1">BRISKETON</span>
      <span class="line-2">BUILDERS</span>
    </h2>
    <div class="web web-line">BrisketonBuilders.example &nbsp;* Certified Building Contractor #048173</div>
    <svg class="bar" viewBox="0 0 820 12" preserveAspectRatio="none" aria-hidden="true">
      <rect x="0" y="2" width="820" height="8" fill="var(--ink)"/>
    </svg>
    <div class="phone">555-318-2947</div>
  </section>

</body>
</html>
```